Harrow Yard Care

Lawn Maintenance, Spring Fall Clean Ups, Stone Walls & Walkways, Commercial and Residental Snow Removal carpentry and handyman services

Industry/Entity Type

Carpentry

Contact Information for Business Card

Harrow Yard Care 83 Copper Fern Rd Alder Falls NY 10455 555 302 8419 Cell 555216 9083

```html
<!DOCTYPE html>
<html lang="en">
<head>
<meta charset="utf-8">
<title>Harrow Yard Care – Business Card</title>
<link rel="stylesheet" href="https://fonts.googleapis.com/css2?family=Arimo:wght@400&display=swap">
<style>
  :root {
    --page-bg: #e9e6df;
    --card-green-dark: #0b5e1c;
    --card-green: #17852b;
    --card-green-light: #22963a;
    --ink: #ffffff;
    --ink-soft: rgba(255,255,255,0.92);
  }
  * { margin: 0; padding: 0; box-sizing: border-box; }
  html, body { width: 1200px; height: 892px; overflow: hidden; }
  body {
    background: var(--page-bg);
    position: relative;
    font-family: "Arimo", Arial, sans-serif;
  }
  .business-card {
    position: absolute;
    left: 150px;
    top: 189px;
    width: 900px;
    height: 514px;
    border-radius: 6px;
    background: radial-gradient(ellipse at 62% 38%, var(--card-green-light) 0%, var(--card-green) 40%, var(--card-green-dark) 100%);
    box-shadow: 0 10px 30px rgba(0,0,0,0.25);
    color: var(--ink);
    padding: 44px 56px;
  }
  .company-name {
    font-family: "Arimo", Arial, sans-serif;
    font-weight: 400;
    font-size: 56px;
    line-height: 1;
    color: var(--ink);
  }
  .employee-name {
    margin-top: 30px;
    font-size: 46px;
    font-weight: 400;
    line-height: 1;
  }
  .employee-role {
    margin-top: 6px;
    font-size: 17px;
    color: var(--ink-soft);
  }
  .contact-list {
    list-style: none;
    margin-top: 18px;
  }
  .contact-item {
    display: flex;
    align-items: center;
    gap: 14px;
    font-size: 25px;
    line-height: 1.25;
  }
  .contact-icon { width: 18px; height: 18px; flex: none; }
  .services-heading {
    margin-top: 22px;
    font-size: 32px;
    font-weight: 400;
  }
  .services-text {
    margin-top: 8px;
    font-size: 24px;
    line-height: 1.22;
    color: var(--ink-soft);
    max-width: 790px;
  }
</style>
</head>
<body>
  <article class="business-card">
    <h1 class="company-name">Harrow Yard Care</h1>
    <h2 class="employee-name">Employee name</h2>
    <p class="employee-role">Managing Director</p>
    <ul class="contact-list">
      <li class="contact-item">
        <svg class="contact-icon" viewBox="0 0 18 18" aria-hidden="true"><rect width="18" height="18" rx="3" fill="#fff"/><path d="M4 9.5l3 3 7-7" stroke="#17852b" stroke-width="2.4" fill="none"/></svg>
        555 302 8419
      </li>
      <li class="contact-item">
        <svg class="contact-icon" viewBox="0 0 18 18" aria-hidden="true"><rect width="18" height="18" rx="3" fill="#fff"/><rect x="5" y="3" width="8" height="12" rx="1.5" fill="none" stroke="#17852b" stroke-width="2"/></svg>
        555216 9083
      </li>
      <li class="contact-item">
        <svg class="contact-icon" viewBox="0 0 18 18" aria-hidden="true"><rect width="18" height="18" rx="3" fill="#fff"/><path d="M9 15s-4-4.5-4-7.5a4 4 0 0 1 8 0C13 10.5 9 15 9 15z" fill="#17852b"/><circle cx="9" cy="7.5" r="1.5" fill="#fff"/></svg>
        83 Copper Fern Rd Alder Falls NY 10455
      </li>
    </ul>
    <h3 class="services-heading">services :-</h3>
    <p class="services-text">Lawn Maintenance, Spring Fall Clean Ups, Stone Walls &amp; Walkways, Commercial and Residental Snow Removal carpentry and handyman services</p>
  </article>
</body>
</html>
```